NEW Website DESIGN for Brightwell Panes & Stoneworks Company

Brand New website, contemporary, clean, visual (images), not busy. ATTACHED IS OUR LOG THAT YOU MUST USE.

The company is called Brightwell Panes & Stoneworks (BrightwellPS)
www.brightwellps.com
The website should be www.brightwellpns.com
one page for glass one page for solid surfaces www.brightwellpanesplashes.co.uk
www.brightwellstoneworkss.co.uk

Target Market(s)

Hotels, Commercial projects, Small focus on residential

Industry/Entity Type

Construction

Number of Pages Required

5+ page

Font styles to use
Sans Serif

Requirements
Must have
• COLOURS AS PER OUR LOGO - WHITE/YELLOW/GREY - WHITE BACK GROUND
• CLEAR SIMPLE NAVIGATION - MODER CLEAN CUT - DESIGN FEEL
• LATEST NAVIGATION FOR IMAGES and text to include per project details
• WORK/PROJECT AREA - NEWS AREA - TEAM AREA/ABOUT US/CONTACT US
• NEW PAGEwww.brightwellpanesplashes.co.uk - NEW PAGE www.brightwellstoneworkss.co.uk
• PLEASE COPY THIS TYPE OF TEMPALTE
• https://www.harlowmead.co.uk/project/grand-halls/
• MOBILE READY
• WORDPRESS
• MODERN IMAGES INCLUDING VELMARA KESTRIN AND GLASS PROJECTS
Nice to have
• NEW DESIGN MODER FRESH
• WEBSITES I LIKE THE TEMPLATE SHOULD BE LIKE THE WEBSITE BELOW
• https://www.harlowmead.co.uk/
Should not have
• NOT Old fashion template, not busy NAVIGATION
• NO BLACK
• NO DARK GREYS
• NOT LOTS OF YELLOW
• RESDENTIAL IMAGES

```html
<!DOCTYPE html>
<html lang="en">
<head>
<meta charset="utf-8">
<title>Brightwell Panes &amp; Stoneworks</title>
<link rel="stylesheet" href="https://fonts.googleapis.com/css2?family=Montserrat:wght@500;600;700;800&family=PT+Sans:wght@400;700&display=swap">
<style>
:root{
  --white:#ffffff;
  --ink:#333333;
  --grey-head:#666666;
  --grey-text:#555555;
  --grey-soft:#8c8c8c;
  --grey-line:#cfcfcf;
  --panel:#ececec;
  --footer:#f6f6f6;
  --yellow:#f5ec1c;
  --yellow-deep:#e2d600;
  --charcoal:#2f2f2f;
  --frame-dark:#000000;
}
*{box-sizing:border-box;margin:0;padding:0}
html,body{width:1200px;height:2643px;overflow:hidden;background:var(--white)}
body{position:relative;font-family:"PT Sans",Arial,sans-serif;color:var(--grey-text)}
.abs{position:absolute}
.heading{font-family:"Montserrat",Arial,sans-serif;font-weight:800;color:var(--grey-head);text-align:center;letter-spacing:1px}
.btn{position:absolute;border-radius:30px;background:linear-gradient(#9a9a9a,#6d6d6d);box-shadow:3px 4px 0 #3d3d3d;color:var(--white);font-family:"Montserrat",Arial,sans-serif;font-weight:700;display:flex;align-items:center;justify-content:center;letter-spacing:.5px}

/* header */
.site-header{left:0;top:0;width:1200px;height:155px;background:var(--white);box-shadow:0 4px 6px rgba(0,0,0,.25);z-index:2}
.brand-mark{left:133px;top:17px;width:100px;height:100px;border-radius:50%;border:12px solid var(--grey-soft)}
.brand-name{left:77px;top:124px;font-family:"Montserrat",Arial,sans-serif;font-weight:600;font-size:18px;color:var(--grey-head)}
.menu-toggle{left:1038px;top:36px;width:84px;height:84px;border-radius:50%;background:#8d8d8d}

/* hero */
.hero{left:0;top:155px;width:1200px;height:573px;background:linear-gradient(90deg,#ececec 0%,#f7f7f7 20%,#fbfbfb 50%,#f4f4f4 80%,#e6e6e6 100%)}
.hero-title{left:0;top:370px;width:1200px;font-size:62px;color:#5d5d5d}
.hero-sub{left:262px;top:458px;width:676px;text-align:center;font-size:15px;line-height:21px;color:#555}

/* projects */
.projects-title{left:0;top:786px;width:1200px;font-size:44px}
.project-photo{top:865px;width:333px;height:478px}
.project-label{top:1247px;width:344px;height:87px;background:var(--yellow);font-family:"Montserrat",Arial,sans-serif;font-weight:700;font-size:30px;color:var(--ink);display:flex;align-items:center;justify-content:center}
.project-active-bar{left:428px;top:900px;width:344px;height:81px;background:var(--charcoal);color:var(--yellow);font-family:"Montserrat",Arial,sans-serif;font-weight:700;font-size:30px;display:flex;align-items:center;justify-content:center}
.project-active-text{left:463px;top:1073px;width:274px;text-align:center;font-size:14px;line-height:24px;color:#555}

/* about */
.about{left:0;top:1427px;width:1200px;height:458px;background:linear-gradient(120deg,#eeeeee,#e6e6e6 50%,#efefef)}
.about-outline{left:62px;top:1454px;width:521px;height:331px;border:2px solid #bdbdbd}
.about-shadow{left:93px;top:1485px;width:522px;height:332px;background:var(--frame-dark)}
.about-photo{left:78px;top:1469px;width:521px;height:332px;background:linear-gradient(180deg,#dfe2e4 0%,#c9d0d5 45%,#e6e6e3 60%,#cfcfcb 100%)}
.about-title{left:646px;top:1496px;font-size:48px;text-align:left}
.about-text{left:645px;top:1558px;width:475px;font-size:14px;line-height:23px;color:#555}

/* news */
.news-title{left:0;top:1944px;width:1200px;font-size:44px}
.news-date{width:74px;text-align:right;color:var(--ink)}
.news-date .day{font-size:21px;line-height:24px}
.news-date .month{font-size:11px;line-height:16px;color:#555;border-bottom:2px solid #666;padding-bottom:6px}
.news-date .views{font-size:11px;color:#555;margin-top:10px}
.news-photo{top:2019px;width:314px;height:157px}
.news-text{top:2195px;width:300px;font-size:14px;line-height:25px;font-weight:700;color:#666}

/* footer */
.site-footer{left:0;top:2303px;width:1200px;height:282px;background:var(--footer)}
.footer-head{top:2364px;font-family:"Montserrat",Arial,sans-serif;font-weight:700;font-size:18px;color:#666}
.footer-links{left:80px;top:2408px;list-style:none;font-size:13px;color:#888;line-height:30px}
.footer-copy{left:448px;top:2406px;width:312px;font-size:13px;line-height:22px;color:#888}
.email-field{left:448px;top:2465px;width:308px;height:39px;border-radius:20px;background:#ececec;box-shadow:inset 0 -2px 0 #777;font-size:13px;color:#777;padding:12px 0 0 22px}
.contact-line{left:870px;font-size:13px;line-height:22px;color:#999;display:flex;gap:8px}
.social{top:2517px;width:52px;height:52px;border-radius:50%;border:1px solid #bbb;background:var(--white)}
.social.primary{background:var(--yellow-deep);border:2px solid #555}
.bottom-bar{left:0;top:2585px;width:1200px;height:58px;background:linear-gradient(#f7ef2a,#d8cc00);display:flex;align-items:center;justify-content:center;font-size:13px;color:#444;gap:6px}
.bottom-bar strong{font-family:"Montserrat",Arial,sans-serif;font-size:17px;color:var(--ink)}
</style>
</head>
<body>

<header class="abs site-header">
  <div class="abs brand-mark"></div>
  <div class="abs brand-name">Brightwell Panes &amp; Stoneworks</div>
  <div class="abs menu-toggle">
    <svg width="84" height="84" viewBox="0 0 84 84">
      <g stroke="#fff" stroke-width="3" stroke-linecap="round">
        <line x1="28" y1="28" x2="58" y2="28"/><line x1="28" y1="37" x2="58" y2="37"/>
        <line x1="28" y1="46" x2="58" y2="46"/><line x1="28" y1="55" x2="58" y2="55"/>
      </g>
      <g fill="#fff"><circle cx="26" cy="28" r="3"/><circle cx="26" cy="37" r="3"/><circle cx="26" cy="46" r="3"/><circle cx="26" cy="55" r="3"/></g>
    </svg>
  </div>
</header>

<section>
  <div class="abs hero" role="img" aria-label="Bright white bathroom with a frameless glass shower enclosure"></div>
  <h1 class="abs heading hero-title">PANES &amp; STONEWORKS</h1>
  <p class="abs hero-sub">Lorem Ipsum is simply dummy text of the printing and typesetting industry. Lorem Ipsum has been the industry's standard dummy text.</p>
</section>

<section>
  <h2 class="abs heading projects-title">OUR PROJECTS</h2>
  <div class="abs project-photo" style="left:78px;background:linear-gradient(160deg,#5a4636 0%,#d8d2c6 40%,#7d8a7e 70%,#cfc9bd 100%)" role="img" aria-label="Kitchen with a green glass worktop and pendant lights"></div>
  <div class="abs project-label" style="left:72px">Project Name</div>

  <div class="abs project-photo" style="left:433px;background:linear-gradient(180deg,#d8d0c2 0%,#f3f1ed 20%,#f6f5f2 100%)" role="img" aria-label="Pale interior with solid surface finishes"></div>
  <div class="abs project-active-bar">Project Name</div>
  <p class="abs project-active-text">Lorem Ipsum is simply dummy text of the printing and typesetting industry. Lorem Ipsum has been the industry's standard dummy text ever since the 1500.</p>
  <div class="btn" style="left:523px;top:1193px;width:154px;height:46px;font-size:16px">VIEW MORE</div>

  <div class="abs project-photo" style="left:789px;background:linear-gradient(180deg,#3c6fb6 0%,#9fbfe0 35%,#6f7f72 60%,#a07a4e 100%)" role="img" aria-label="Terrace with glass balustrade overlooking the countryside"></div>
  <div class="abs project-label" style="left:784px">Project Name</div>
</section>

<section>
  <div class="abs about" role="img" aria-label="Soft white marble background"></div>
  <div class="abs about-outline"></div>
  <div class="abs about-shadow"></div>
  <div class="abs about-photo" role="img" aria-label="Empty bright office floor with glass partitions"></div>
  <h2 class="abs heading about-title">ABOUT US</h2>
  <p class="abs about-text">Lorem Ipsum is simply dummy text of the printing and typesetting industry. Lorem Ipsum has been the industry's standard dummy text ever since the 1500s, when an unknown printer took a galley of type and scrambled it to make a type specimen book. It has survived not only five centuries, but also the leap into electronic typesetting, remaining essentially unchanged. It was popularised in the 1960s.</p>
  <div class="btn" style="left:643px;top:1720px;width:183px;height:44px;font-size:16px">LEARN MORE</div>
</section>

<section>
  <h2 class="abs heading news-title">LATEST NEWS</h2>

  <div class="abs news-date" style="left:188px;top:2037px">
    <div class="day">29</div><div class="month">Aug - 2018</div>
    <div class="views"><svg width="18" height="11" viewBox="0 0 18 11" style="display:block;margin:0 0 2px auto"><path d="M1 5.5C4 0 14 0 17 5.5C14 11 4 11 1 5.5Z" fill="#333"/><circle cx="9" cy="5.5" r="2.3" fill="#fff"/></svg>20 - View</div>
  </div>
  <div class="abs news-photo" style="left:271px;background:linear-gradient(180deg,#8fb5bd 0%,#a9c8cd 55%,#e4e4e4 65%,#d2d4d4 100%)" role="img" aria-label="Water droplets on glass above white marble"></div>
  <p class="abs news-text" style="left:276px">Lorem ipsum dolor sit amet, consectetur adipiscing elit, sed do eiusmod tempor</p>

  <div class="abs news-date" style="left:615px;top:2037px">
    <div class="day">29</div><div class="month">Aug - 2018</div>
    <div class="views"><svg width="18" height="11" viewBox="0 0 18 11" style="display:block;margin:0 0 2px auto"><path d="M1 5.5C4 0 14 0 17 5.5C14 11 4 11 1 5.5Z" fill="#333"/><circle cx="9" cy="5.5" r="2.3" fill="#fff"/></svg>20 - View</div>
  </div>
  <div class="abs news-photo" style="left:700px;background:linear-gradient(135deg,#8a8580 0%,#d9d4cb 35%,#6a6560 60%,#4a4744 100%)" role="img" aria-label="Close-up of speckled solid surface samples"></div>
  <p class="abs news-text" style="left:703px">Lorem ipsum dolor sit amet, consectetur adipiscing elit, sed do eiusmod tempor</p>
</section>

<footer>
  <div class="abs site-footer"></div>
  <h3 class="abs footer-head" style="left:80px">Navigation</h3>
  <ul class="abs footer-links"><li>Home</li><li>About Us</li><li>Projects</li><li>Blogs</li><li>Contact Us</li></ul>

  <h3 class="abs footer-head" style="left:448px">Keep In Touch</h3>
  <p class="abs footer-copy">Lorem ipsum dolor sit amet, consectetur adipiscing elit, sed do eiusmod tempor</p>
  <div class="abs email-field">Email</div>
  <div class="btn" style="left:444px;top:2513px;width:158px;height:47px;font-size:19px">SUBMIT</div>

  <h3 class="abs footer-head" style="left:871px">Contact Us</h3>
  <div class="abs contact-line" style="top:2408px">
    <svg width="14" height="20" viewBox="0 0 14 20"><path d="M7 0C3 0 0 3 0 7c0 5 7 13 7 13s7-8 7-13c0-4-3-7-7-7z" fill="#aaa"/><circle cx="7" cy="7" r="2.5" fill="#f6f6f6"/></svg>
    <span>123, Lorem ipsum dummy text,<br>Country - 123456.</span>
  </div>
  <div class="abs contact-line" style="top:2470px">
    <svg width="16" height="16" viewBox="0 0 16 16"><path d="M3 0l3 3-2 2c1 3 4 6 7 7l2-2 3 3-2 3C7 15 1 9 0 3z" fill="#aaa"/></svg>
    <span>123 456 7878</span>
  </div>
  <div class="abs social primary" style="left:874px"></div>
  <div class="abs social" style="left:936px"></div>
  <div class="abs social" style="left:996px"></div>

  <div class="abs bottom-bar">© <strong>Brightwell Panes &amp; Stoneworks</strong> - 2018. All Rights Reserved</div>
</footer>

</body>
</html>
```